Business Card Design Project

The business card is for an educational company that provides personalised tuition to students.

The company logo is in orange and blue (as provided) and should be included in the name card design

The philosophy of the company is to make learning a comfortable experience for student as such design of the namecard should look fresh and has a bit of the 'wow' factor. Some of the namecard design that appeals to me are as uploaded under Sample Design.

The particulars that need to be provided are:
(1): Company Name (Quillmont Education)
(1): Name
(2): Educational qualifications which will appear below name
(3): Mobile number
(4): Email address
(5): Website

Industry/Entity Type

Business

Requirements
Must have
• (1): Company Logo

(2): The card background should preferably be coloured both for the front side and back.

(3): The choice of font is important as part of the selection consideration. There is no preferred font that I have selected, designer is free to choose the font that will complement their design.

```html
<!DOCTYPE html>
<html lang="en">
<head>
<meta charset="utf-8">
<title>Quillmont Education — Business Card</title>
<link rel="stylesheet" href="https://fonts.googleapis.com/css2?family=Libre+Baskerville:wght@400;700&family=Open+Sans:wght@400;600;700&display=swap">
<style>
  :root {
    --page-bg: #e4e4e2;
    --card-light: #fffdf7;
    --card-cream: #f3ecd6;
    --card-gold: #d9c88f;
    --pattern-gold: rgba(214, 190, 110, 0.38);
    --pattern-pale: rgba(240, 228, 185, 0.25);
    --bird-pink: #d8406e;
    --bird-olive: #a8a03a;
    --bird-green: #6f9a3c;
    --brand-grey: #5d5d5d;
    --brand-square: #f07a22;
    --ink: #1e1e1e;
    --ink-soft: #333333;
  }

  * { box-sizing: border-box; margin: 0; padding: 0; }

  html, body {
    width: 1200px;
    height: 861px;
    overflow: hidden;
  }

  body {
    background: var(--page-bg);
    position: relative;
    font-family: "Open Sans", Arial, sans-serif;
  }

  .card {
    position: absolute;
    top: 262px;
    width: 520px;
    height: 336px;
    border-radius: 14px;
    overflow: hidden;
    background: radial-gradient(ellipse at 50% 50%, var(--card-light) 0%, var(--card-cream) 60%, var(--card-gold) 130%);
    box-shadow: 0 10px 30px rgba(0, 0, 0, 0.18);
  }

  .card--front { left: 50px; }
  .card--back  { left: 630px; }

  .paisley-pattern {
    position: absolute;
    inset: 0;
    background:
      radial-gradient(circle at 78% 30%, var(--pattern-gold) 0%, transparent 32%),
      radial-gradient(circle at 60% 88%, var(--pattern-gold) 0%, transparent 28%),
      radial-gradient(circle at 18% 80%, var(--pattern-pale) 0%, transparent 30%),
      radial-gradient(circle at 95% 75%, var(--pattern-gold) 0%, transparent 25%);
  }

  .bird-motif {
    position: absolute;
    border-radius: 40% 55% 45% 50%;
    background:
      radial-gradient(circle at 62% 30%, rgba(216, 64, 110, 0.55) 0%, transparent 35%),
      radial-gradient(circle at 40% 65%, rgba(168, 160, 58, 0.55) 0%, transparent 45%),
      radial-gradient(circle at 20% 30%, rgba(111, 154, 60, 0.4) 0%, transparent 40%);
  }

  .card--front .bird-motif { left: 0; top: 0; width: 240px; height: 240px; }
  .card--back  .bird-motif { right: 0; top: 10px; width: 190px; height: 170px; }

  .brand {
    position: absolute;
    display: flex;
    align-items: center;
    gap: 12px;
  }

  .brand__mark {
    width: 62px;
    height: 62px;
    background: var(--brand-square);
    flex: none;
  }

  .brand__name {
    font-family: "Libre Baskerville", Georgia, serif;
    font-weight: 400;
    font-size: 26px;
    line-height: 1.05;
    color: var(--brand-grey);
  }

  .card--front .brand { left: 250px; top: 120px; }
  .card--back  .brand { left: 50px;  top: 44px; }

  .front__website {
    position: absolute;
    left: 268px;
    top: 202px;
    font-weight: 700;
    font-size: 17px;
    color: var(--ink);
  }

  .holder {
    position: absolute;
    left: 52px;
    top: 144px;
  }

  .holder__name {
    font-family: "Libre Baskerville", Georgia, serif;
    font-weight: 700;
    font-size: 27px;
    color: var(--ink);
  }

  .holder__credentials {
    font-size: 14px;
    font-weight: 600;
    margin-left: 4px;
  }

  .holder__role {
    font-size: 17px;
    color: var(--ink-soft);
    margin-top: 2px;
  }

  .contacts {
    position: absolute;
    left: 52px;
    top: 226px;
    display: grid;
    grid-template-columns: 86px auto;
    row-gap: 2px;
    font-size: 16px;
    color: var(--ink-soft);
  }

  .contacts dt { font-weight: 700; color: var(--ink); }
  .contacts dd::before { content: ": "; }
</style>
</head>
<body>

  <section class="card card--front" aria-label="Card front">
    <div class="paisley-pattern" role="img" aria-label="Gold paisley and floral pattern"></div>
    <div class="bird-motif" role="img" aria-label="Ornamental bird illustration with pink and olive feathers among leafy sprigs"></div>
    <div class="brand">
      <span class="brand__mark"></span>
      <span class="brand__name">Quillmont<br>Education</span>
    </div>
    <p class="front__website">www.quillmont-edu.com</p>
  </section>

  <section class="card card--back" aria-label="Card back">
    <div class="paisley-pattern" role="img" aria-label="Gold paisley and floral pattern"></div>
    <div class="bird-motif" role="img" aria-label="Ornamental bird illustration with pink and olive feathers among leafy sprigs"></div>
    <div class="brand">
      <span class="brand__mark"></span>
      <span class="brand__name">Quillmont<br>Education</span>
    </div>
    <div class="holder">
      <h1 class="holder__name">Tan Wei Ming <span class="holder__credentials">PhD, Bsc (Hons)</span></h1>
      <p class="holder__role">Senior Tutor</p>
    </div>
    <dl class="contacts">
      <dt>Mobile</dt><dd>+65 90031427</dd>
      <dt>Email</dt><dd>wmtan@quillmont-edu.com</dd>
      <dt>Website</dt><dd>www.quillmont-edu.com</dd>
    </dl>
  </section>

</body>
</html>
```